Brantley Advisory Group provides support for renewable energy projects to utilities and suppliers

I need a professional looking business card that is both simple and elegant and unique. My clients are mostly large organizations not individuals. I am a consultant with my own company that is small but would like to give clients the impression I am larger. Smart grid, fiber optics, software, field hardware, distribution automation, substation automation, operations, energy storage/batteries, microgrids, customer service, strategy/roadmaps, conservation, Automated Metering Infrastruture (AMI or smart meters) are all areas of focus.

Target Market(s)

Utilities, suppliers, governmental agencies involved in energy. All types of energy especially natural gas and electrical. Especially renewable energy or green projects.

Contact Information for Business Card

Name - Mark Brantley Cell Phone - 425.318.2746 Email - mbrantley@brantleyag-example.com
Company - Brantley Advisory Group (logo) Title - Principal

Font styles to use
Serif
Sans Serif

Colors

Designer to choose colors to be used in the design.

Requirements
Must have
• Simple and professional and powerful.
• Unique/creative design.
Nice to have
• Utilize color scheme to accent logo colors. Maybe some geometric pattern on edge of card with color.
Should not have
• Busy, complicated, traditional

```html
<!DOCTYPE html>
<html lang="en">
<head>
<meta charset="UTF-8">
<title>Brantley Advisory Group – Business Card</title>
<link href="https://fonts.googleapis.com/css2?family=Open+Sans:wght@400;700&family=Merriweather:wght@700;900&display=swap" rel="stylesheet">
<style>
  :root {
    --page-bg: #1c1c1e;
    --card-white: #ffffff;
    --pattern-light: #f3f3f3;
    --pattern-mid: #e2e2e2;
    --back-light: #dcdcdc;
    --back-mid: #bdbdbd;
    --brand-navy: #2b3595;
    --ink: #2a2a2a;
    --title-grey: #5b5b66;
  }
  * { box-sizing: border-box; margin: 0; padding: 0; }
  html, body { width: 1200px; height: 900px; overflow: hidden; }
  body {
    background: var(--page-bg);
    font-family: "Open Sans", Arial, sans-serif;
    position: relative;
  }
  .card {
    position: absolute;
    left: 250px;
    width: 700px;
    height: 400px;
    border-radius: 26px;
    overflow: hidden;
  }
  .card--front { top: 40px; background: var(--card-white); }
  .card--back { top: 460px; background: var(--back-light); }

  .card__pattern {
    position: absolute; inset: 0;
  }
  .card--front .card__pattern {
    background: linear-gradient(135deg, var(--card-white) 0%, var(--pattern-light) 50%, var(--card-white) 100%);
  }
  .card--back .card__pattern {
    background: linear-gradient(160deg, var(--back-light) 0%, var(--back-mid) 55%, var(--back-light) 100%);
  }

  .brand {
    position: absolute;
    display: flex;
    align-items: center;
    gap: 14px;
    color: var(--brand-navy);
    font-weight: 700;
    white-space: nowrap;
  }
  .brand__mark { background: var(--brand-navy); flex: none; }
  .card--front .brand { left: 250px; top: 70px; font-size: 30px; }
  .card--front .brand__mark { width: 30px; height: 30px; }
  .card--back .brand { left: 50%; top: 50%; transform: translate(-50%, -50%); font-size: 44px; }
  .card--back .brand__mark { width: 44px; height: 44px; }

  .person {
    position: absolute;
    left: 250px;
    top: 140px;
    font-family: "Merriweather", Georgia, serif;
  }
  .person__name { font-size: 34px; font-weight: 900; color: var(--ink); }
  .person__title {
    display: inline-block;
    margin-top: 2px;
    font-size: 22px;
    font-weight: 700;
    color: var(--title-grey);
    border-bottom: 2px solid var(--title-grey);
  }

  .contact {
    position: absolute;
    display: flex;
    align-items: center;
    gap: 14px;
    font-size: 21px;
    color: var(--ink);
  }
  .contact__icon { width: 30px; height: 30px; flex: none; }
  .contact--phone { left: 50px; top: 60px; }
  .contact--email { left: 250px; top: 310px; }
</style>
</head>
<body>
  <section class="card card--front" aria-label="Business card front">
    <div class="card__pattern" role="img" aria-label="Soft grey chevron pattern background"></div>
    <div class="contact contact--phone">
      <svg class="contact__icon" viewBox="0 0 24 24" aria-hidden="true"><path fill="#2a2a2a" d="M6.6 10.8a15.1 15.1 0 0 0 6.6 6.6l2.2-2.2c.3-.3.7-.4 1-.2 1.1.4 2.3.6 3.6.6.6 0 1 .4 1 1V20c0 .6-.4 1-1 1A17 17 0 0 1 3 4c0-.6.4-1 1-1h3.5c.6 0 1 .4 1 1 0 1.3.2 2.5.6 3.6.1.3 0 .7-.2 1z"/></svg>
      <span>425.318.2746</span>
    </div>
    <div class="brand">
      <span class="brand__mark"></span>
      <span class="brand__name">Brantley Advisory Group</span>
    </div>
    <div class="person">
      <p class="person__name">Mark Brantley</p>
      <p class="person__title">Principal</p>
    </div>
    <div class="contact contact--email">
      <svg class="contact__icon" viewBox="0 0 24 24" aria-hidden="true"><rect x="2" y="5" width="20" height="14" fill="#2a2a2a"/><path d="M2.5 5.5 12 13l9.5-7.5M2.5 18.5l7-6.5M21.5 18.5l-7-6.5" stroke="#fff" stroke-width="1.3" fill="none"/></svg>
      <span>mbrantley@brantleyag-example.com</span>
    </div>
  </section>

  <section class="card card--back" aria-label="Business card back">
    <div class="card__pattern" role="img" aria-label="Grey geometric triangle pattern background"></div>
    <div class="brand">
      <span class="brand__mark"></span>
      <span class="brand__name">Brantley Advisory Group</span>
    </div>
  </section>
</body>
</html>
```